Statement of Professional Excellence

Our school community has create a statement of Professional Excellence at our school (TBS = The Birchfield School at Dunmore) This will be shared internally and with candidates interviewing at our school. We'd like a branded graphic that lists in an interesting way our statements:

Professional Excellence at TBS

We honor the whole child while embracing them where they are.
We are mission-driven individuals whose dedication to our students motivates our daily work.
We bring flexible thinking to allow the needs of the students to drive the learning.
We are patient, nurturing, empathetic, and compassionate people.
We value, trust, and support each other.
We learn and we teach.
We lean into and celebrate diversity.
We build trust through genuine partnerships with families.
We are quirky, fun and proud of it.

```html
<!DOCTYPE html>
<html lang="en">
<head>
<meta charset="utf-8">
<title>Professional Excellence at TBS</title>
<link rel="stylesheet" href="https://fonts.googleapis.com/css2?family=Lora:ital,wght@0,500;1,400;1,700&display=swap">
<style>
  :root {
    --ink: #000000;
    --gold: #e2bf3a;
    --gold-text: #dcb838;
    --navy: #243850;
    --silver-light: #ffffff;
    --silver-mid: #a9abb1;
    --silver-dark: #55575c;
  }
  * { margin: 0; padding: 0; box-sizing: border-box; }
  html, body { width: 927px; height: 1200px; overflow: hidden; background: var(--ink); }
  .poster {
    position: relative;
    width: 927px;
    height: 1200px;
    background: var(--ink);
    overflow: hidden;
  }
  .backdrop { position: absolute; inset: 0; }
  .poster-title {
    position: absolute;
    top: 74px;
    left: 0;
    width: 100%;
    padding-left: 14px;
    text-align: center;
    font-family: "Lora", Georgia, serif;
    font-style: italic;
    font-weight: 700;
    font-size: 56px;
    letter-spacing: 0.5px;
    color: var(--gold);
  }
  .statements {
    position: absolute;
    top: 206px;
    left: 0;
    width: 100%;
    padding-left: 14px;
    list-style: none;
    text-align: center;
    font-family: "Lora", Georgia, serif;
    font-style: italic;
    font-weight: 400;
    font-size: 25px;
    line-height: 31.3px;
    color: var(--gold-text);
  }
  .statements li + li { margin-top: 30.7px; }
  .school-name {
    position: absolute;
    top: 1036px;
    left: 0;
    width: 100%;
    padding-left: 14px;
    text-align: center;
    font-family: "Lora", Georgia, serif;
    font-weight: 500;
    font-size: 30px;
    line-height: 38px;
    color: var(--navy);
  }
</style>
</head>
<body>
<main class="poster">
  <svg class="backdrop" width="927" height="1200" viewBox="0 0 927 1200" aria-hidden="true">
    <defs>
      <linearGradient id="sheen-left" x1="0" y1="0" x2="1" y2="0">
        <stop offset="0" stop-color="var(--silver-light)"/>
        <stop offset="0.12" stop-color="var(--silver-mid)"/>
        <stop offset="0.3" stop-color="var(--silver-dark)"/>
        <stop offset="0.5" stop-color="#000"/>
      </linearGradient>
      <linearGradient id="sheen-right" x1="1" y1="0" x2="0" y2="0">
        <stop offset="0" stop-color="var(--silver-light)"/>
        <stop offset="0.12" stop-color="var(--silver-mid)"/>
        <stop offset="0.3" stop-color="var(--silver-dark)"/>
        <stop offset="0.5" stop-color="#000"/>
      </linearGradient>
      <linearGradient id="panel-fade" x1="0" y1="0" x2="1" y2="0">
        <stop offset="0" stop-color="#000" stop-opacity="0"/>
        <stop offset="0.05" stop-color="#000" stop-opacity="1"/>
        <stop offset="0.95" stop-color="#000" stop-opacity="1"/>
        <stop offset="1" stop-color="#000" stop-opacity="0"/>
      </linearGradient>
    </defs>
    <!-- outer side curves -->
    <ellipse cx="440" cy="600" rx="440" ry="900" fill="url(#sheen-left)"/>
    <ellipse cx="487" cy="600" rx="440" ry="900" fill="url(#sheen-right)" opacity="0.9"/>
    <!-- inner side curves -->
    <ellipse cx="470" cy="545" rx="418" ry="455" fill="url(#sheen-left)"/>
    <ellipse cx="457" cy="545" rx="418" ry="455" fill="url(#sheen-right)" opacity="0.9"/>
    <!-- central panel -->
    <rect x="92" y="0" width="743" height="1200" fill="url(#panel-fade)"/>
  </svg>

  <h1 class="poster-title">Professional Excellence</h1>

  <ul class="statements">
    <li>We honor<br>The whole child while embracing them where they are.</li>
    <li>We are mission-driven Individuals whose<br>dedication to our students motivates our daily work.</li>
    <li>We bring flexible thinking to allow<br>the needs of the students to drive the learning.</li>
    <li>We are patient, nurturing,<br>empathetic, and compassionate people.</li>
    <li>We value, trust, and support each other.</li>
    <li>We learn and we teach.</li>
    <li>We lean into and celebrate diversity.</li>
    <li>We build trust through genuine partnerships<br>with families.</li>
    <li>We are quirky, fun and proud of it.</li>
  </ul>

  <p class="school-name">The Birchfield School<br>at Dunmore</p>
</main>
</body>
</html>
```